Create a Eye Catching Web Design

We need an informative web design that needs to be eye catching and unique. All of the information needs to be on that page - We have a shopfront setup in the next 2 weeks so the website needs to be ready asap. We are selling mainly rehabilitation aids and mobility products.

The website is main purpose is to inform customers about our range of products, address and phone number. This is an interim website until we get an ecommerce website setup. We are not looking for an ecommerce website, just simple, eye-catching and informative. clean, crisp and modern -target age 45-75 yo (men and women)

I have included our logo and brochure designed with our range of product categories.

The website needs to be designed, coded and setup completely as a finished product.

As soon as the website design is chosen, the chosen designer would need to get the website up and running. If the website design is chosen and great, we could use the same designer for the ecommerce build as well.

www.tolvenacare.com
www.tolvenacare.com.au

Reason: I haven't received as many designs but variations from the same designers.

Target Market(s)

45-75

Industry/Entity Type

Health And Wellness

Coding

Coded - Design and coding required

Number of Pages Required

2 page

Font styles to use
Sans Serif

Requirements
Nice to have
• clean design, modern feel - not cluttered - something unique. for the market age

```html
<!DOCTYPE html>
<html lang="en">
<head>
<meta charset="utf-8">
<title>Tolvena Care – Rehabilitation &amp; Mobility</title>
<link href="https://fonts.googleapis.com/css2?family=Open+Sans:wght@400;600;700&family=Raleway:wght@300;400;600&display=swap" rel="stylesheet">
<style>
:root{
  --red:#e2141f;
  --green:#4aa32a;
  --green-dark:#3b8b20;
  --ink:#222;
  --text:#555;
  --muted:#888;
  --line:#e3e3e3;
  --grey-bg:#ececec;
  --topbar:#f3f3f3;
  --white:#fff;
}
*{box-sizing:border-box;margin:0;padding:0}
html,body{width:1200px;height:4891px;overflow:hidden}
body{font-family:"Open Sans",Arial,sans-serif;color:var(--text);background:var(--white);position:relative}
.abs{position:absolute}
.brand{font-family:"Open Sans",Arial,sans-serif;font-weight:700;color:var(--red);display:flex;align-items:center;gap:12px}
.brand .dot{border-radius:50%;background:var(--red);display:block}

.topbar{top:0;left:0;width:1200px;height:40px;background:var(--topbar);border-bottom:1px solid var(--line);font-size:12px}
.topbar .mail{left:130px;top:12px}
.topbar .follow{right:120px;top:8px;display:flex;align-items:center;gap:10px}
.social{width:24px;height:24px;background:#e2e2e2;border-radius:3px;display:block}

.header{top:40px;left:0;width:1200px;height:122px}
.header .brand{left:130px;top:34px;font-size:38px}
.header .brand .dot{width:34px;height:34px}
.search{left:483px;top:36px;width:356px;height:46px;border:1px solid #ccc;display:flex;font-size:12px;color:var(--muted)}
.search .cat{width:110px;border-right:1px solid #ccc;padding:14px}
.search .q{flex:1;padding:14px}
.search svg{margin:13px}
.phone{left:893px;top:30px;display:flex;gap:12px;align-items:center}
.phone .num{font-size:26px;color:var(--red);line-height:1}
.phone .sub{font-size:10px;color:var(--muted);letter-spacing:.5px}

.nav{top:162px;left:0;width:1200px;height:36px;background:var(--green)}
.nav ul{list-style:none;display:flex;justify-content:center;height:36px}
.nav li{color:#fff;font-size:12px;font-weight:600;padding:0 31px;line-height:36px}
.nav li.on{background:var(--green-dark)}

.hero{top:198px;left:0;width:1200px;height:532px;background:linear-gradient(180deg,#6f8f3c 0%,#8fae4a 35%,#5f8a2a 70%,#7ea53a 100%)}
.hero-caption{left:630px;top:148px;width:440px;height:130px;background:rgba(0,0,0,.55);padding:20px 26px;color:#fff}
.hero-caption h1{font-size:33px;font-weight:700;letter-spacing:1px;line-height:1.1}
.hero-caption p{font-size:31px;font-weight:400;line-height:1.2}
.btn-red{background:var(--red);color:#fff;font-size:14px;font-weight:600;padding:12px 18px}
.hero .btn-red{left:930px;top:310px}
.dots{left:560px;top:505px;display:flex;gap:8px}
.dots span{width:12px;height:12px;border-radius:50%;background:rgba(255,255,255,.7)}

.cats{top:730px;left:0;width:1200px;height:135px;display:flex;border-bottom:1px solid var(--line)}
.cat-tile{flex:1;display:flex;align-items:center;justify-content:center;gap:16px;border-right:1px solid var(--line);color:var(--red)}
.cat-tile svg{width:58px;height:52px;flex:none}
.cat-tile b{display:block;font-size:19px;font-weight:600;color:var(--ink)}
.cat-tile span{font-size:17px;color:var(--text)}
.cat-tile.active{background:var(--red);color:#fff}
.cat-tile.active b,.cat-tile.active span{color:#fff}

.welcome{top:865px;left:0;width:1200px;height:455px;background:var(--grey-bg)}
.welcome h2{left:132px;top:78px;font-family:"Raleway",sans-serif;font-weight:400;font-size:26px;color:var(--ink)}
.welcome .intro{left:132px;top:150px;width:240px;font-size:13px;line-height:1.85}
.btn-green{background:var(--green);color:#fff;font-size:13px;font-weight:600;padding:12px 22px;display:inline-flex;align-items:center;gap:14px}
.welcome .btn-green{left:136px;top:340px}
.feature{left:478px;width:290px;display:flex;gap:22px}
.feature svg{width:46px;height:42px;flex:none;color:var(--red)}
.feature h4{font-size:12px;color:var(--ink);font-weight:700;margin-bottom:10px}
.feature p{font-size:12px;line-height:1.8}
.feature-sep{left:478px;width:290px;height:1px;background:#d6d6d6}
.welcome .mark{left:840px;top:115px;width:250px;height:250px;border-radius:50%;background:var(--red)}

.section-title{left:0;width:1200px;text-align:center;font-family:"Raleway",sans-serif;font-weight:400;color:var(--red);font-size:40px}
.title-rule{left:562px;width:76px;height:1px;background:#ccc}
.photo{background:radial-gradient(ellipse at center,#d9d9d9 0%,#f2f2f2 60%,#fff 100%)}
.product h3{font-family:"Raleway",sans-serif;font-weight:400;font-size:23px;color:var(--ink);margin-bottom:22px}
.product p{font-size:13px;line-height:1.85;width:330px;margin-bottom:22px}

.testi{top:3670px;left:0;width:1200px;height:592px;background:var(--grey-bg)}
.testi .section-title{top:48px}
.arrow-c{width:48px;height:48px;border:2px solid #b5b5b5;border-radius:50%;display:flex;align-items:center;justify-content:center}
.avatar{left:545px;top:160px;width:110px;height:110px;border-radius:50%;background:linear-gradient(135deg,#2d4a5e,#9fb3bd)}
.quote{left:360px;top:330px;width:480px;text-align:center;font-size:15.5px;line-height:2.1;color:#666}
.qmark{font-family:Georgia,serif;font-size:110px;color:#c9c9c9;line-height:1}

.news h2{top:4265px}
.news .sub{top:4325px;left:0;width:1200px;text-align:center;font-size:15px;letter-spacing:2px;color:#666}
.field{top:4383px;height:56px;border:1px solid #ccc;font-size:13px;color:var(--muted);padding:18px 22px}
.news .btn-red{left:771px;top:4383px;width:134px;height:56px;font-size:15px;text-align:center;padding:17px 0}

.footer{top:4512px;left:0;width:1200px;height:298px;border-top:1px solid var(--line)}
.footer .brand{left:132px;top:66px;font-size:38px}
.footer .brand .dot{width:34px;height:34px}
.fhead{font-size:11px;font-weight:700;color:var(--red);letter-spacing:.5px}
.fline{font-size:12px;color:#666;display:flex;gap:18px;align-items:center}
.fmenu{font-size:12px;color:#666;line-height:24.5px;list-style:none}
.follow-row{left:132px;top:196px;display:flex;align-items:center;gap:8px;font-size:11px;font-weight:700;color:var(--red)}
.follow-row i{width:26px;height:26px;border-radius:50%;background:#8fb0e0;display:block}
.copy{top:4810px;left:0;width:1200px;height:81px;border-top:1px solid var(--line);font-size:11px;color:#666;text-align:center;padding-top:32px}
</style>
</head>
<body>

<div class="abs topbar">
  <div class="abs mail">✉ &nbsp;E-mail us : info@tolvenacare.com</div>
  <div class="abs follow">Follow us on : <i class="social"></i><i class="social"></i><i class="social"></i><i class="social"></i></div>
</div>

<header class="abs header">
  <div class="abs brand"><span>TOLVENA CARE</span><i class="dot"></i></div>
  <div class="abs search">
    <div class="cat">Categories ▾</div><div class="q">Search</div>
    <svg width="18" height="18" viewBox="0 0 18 18"><circle cx="7" cy="7" r="5.5" fill="none" stroke="#333" stroke-width="2"/><line x1="11" y1="11" x2="16" y2="16" stroke="#333" stroke-width="2"/></svg>
  </div>
  <div class="abs phone">
    <svg width="36" height="36" viewBox="0 0 24 24"><path d="M6.6 10.8a15 15 0 0 0 6.6 6.6l2.2-2.2a1 1 0 0 1 1-.25 11.4 11.4 0 0 0 3.6.57 1 1 0 0 1 1 1V20a1 1 0 0 1-1 1A17 17 0 0 1 3 4a1 1 0 0 1 1-1h3.5a1 1 0 0 1 1 1c0 1.25.2 2.450.57 3.57a1 1 0 0 1-.25 1z" fill="#e2141f"/></svg>
    <div><div class="num">55014392</div><div class="sub">WE ARE HERE TO HELP</div></div>
  </div>
</header>

<nav class="abs nav"><ul>
  <li class="on">HOME</li><li>ABOUT US</li><li>SERVICES</li><li>REHABILITATION AIDS</li><li>MOBILITY</li><li>BLOG</li><li>CONTACT US</li>
</ul></nav>

<section class="abs hero" role="img" aria-label="Photo of a smiling woman pushing an elderly woman in a wheelchair through a leafy park">
  <div class="abs hero-caption"><h1>TOLVENA CARE OFFER</h1><p>a wide range of mobility</p></div>
  <div class="abs btn-red">READ MORE &nbsp;›</div>
  <div class="abs dots"><span></span><span></span><span></span><span></span></div>
</section>

<section class="abs cats">
  <div class="cat-tile active">
    <svg viewBox="0 0 58 52" fill="currentColor"><path d="M10 6h8l8 24h20a4 4 0 0 1 4 4v4H22L10 10z"/><rect x="22" y="40" width="28" height="4"/><rect x="24" y="44" width="4" height="6"/><rect x="44" y="44" width="4" height="6"/></svg>
    <div><b>MASSAGE</b><span>Recliners</span></div></div>
  <div class="cat-tile">
    <svg viewBox="0 0 58 52" fill="none" stroke="currentColor" stroke-width="4"><path d="M8 36V20a14 14 0 0 1 14-14h14l14 18v12z"/><circle cx="17" cy="40" r="6" fill="#fff"/><circle cx="42" cy="40" r="6" fill="#fff"/></svg>
    <div><b>ELECTRIC</b><span>Scooters</span></div></div>
  <div class="cat-tile">
    <svg viewBox="0 0 58 52" fill="none" stroke="currentColor" stroke-width="4" stroke-linecap="round"><path d="M16 48V10h26v38M16 22h26M16 10c0-4 2-6 6-6"/><circle cx="16" cy="48" r="2" fill="currentColor"/><circle cx="42" cy="48" r="2" fill="currentColor"/></svg>
    <div><b>WALKING</b><span>Aids</span></div></div>
  <div class="cat-tile">
    <svg viewBox="0 0 58 52" fill="none" stroke="currentColor" stroke-width="4" stroke-linecap="round"><path d="M14 6v42M44 6v42M14 26h30M14 18h30M14 34h30"/></svg>
    <div><b>LIVING</b><span>Aids</span></div></div>
  <div class="cat-tile">
    <svg viewBox="0 0 58 52" fill="none" stroke="currentColor" stroke-width="4" stroke-linejoin="round"><rect x="4" y="6" width="50" height="40" rx="3"/><path d="M10 28h10l4-10 6 18 5-12 3 4h8"/></svg>
    <div><b>CONSUMER</b><span>Health</span></div></div>
</section>

<section class="abs welcome">
  <h2 class="abs">Welcome to our site</h2>
  <p class="abs intro">It is a long established fact that a reader will be distracted by the readable content of a page when looking at its layout. The point of using Lorem Ipsum is that it has a more-or-less normal distribution of letters, as opposed</p>
  <div class="abs btn-green">READ MORE</div>
  <div class="abs feature" style="top:78px">
    <svg viewBox="0 0 46 42" fill="none" stroke="currentColor" stroke-width="3" stroke-linejoin="round"><path d="M6 14l17-8 17 8v18l-17 8-17-8z"/><path d="M6 14l17 8 17-8M23 22v18"/></svg>
    <div><h4>LARGE PRODUCT RANGE</h4><p>It is a long established fact that a reader will be distracted.</p></div></div>
  <div class="abs feature-sep" style="top:172px"></div>
  <div class="abs feature" style="top:195px">
    <svg viewBox="0 0 46 42" fill="currentColor"><path d="M23 38 6 21a10 10 0 0 1 17-13 10 10 0 0 1 17 13z"/></svg>
    <div><h4>50 YEARS OF EXPERIENCE</h4><p>It is a long established fact that a reader will be distracted.</p></div></div>
  <div class="abs feature-sep" style="top:300px"></div>
  <div class="abs feature" style="top:335px">
    <svg viewBox="0 0 24 24" fill="none" stroke="currentColor" stroke-width="1.8" stroke-linejoin="round"><path d="M6.6 10.8a15 15 0 0 0 6.6 6.6l2.2-2.2 4.6 1.3V21A17 17 0 0 1 3 4h4.5l1.3 4.6z"/><path d="M14 3h7v5h-4l-3 2z"/></svg>
    <div><h4>GET SUPPORT</h4><p>It is a long established fact that a reader will be distracted.</p></div></div>
  <div class="abs mark"></div>
</section>

<h2 class="abs section-title" style="top:1378px">Our Products</h2>
<div class="abs title-rule" style="top:1462px"></div>

<div class="abs photo" style="left:225px;top:1530px;width:280px;height:320px" role="img" aria-label="Red and cream massage recliner chair"></div>
<div class="abs product" style="left:608px;top:1560px"><h3>Massage Recliners</h3><p style="width:230px">Suffering from Muscle Aches?<br>Receive the perfect massage</p><div class="btn-green">READ MORE &nbsp;›</div></div>

<div class="abs product" style="left:262px;top:2005px"><h3>Electric Scooters</h3><p>Get back your freedom with our range of foldable to high performance electric scooters.</p><div class="btn-green">READ MORE &nbsp;›</div></div>
<div class="abs photo" style="left:615px;top:1915px;width:340px;height:360px" role="img" aria-label="Covered four-wheel electric mobility scooter"></div>

<div class="abs photo" style="left:225px;top:2390px;width:290px;height:330px" role="img" aria-label="Folding wheelchair with leg rests"></div>
<div class="abs product" style="left:612px;top:2395px"><h3>Walking Aids</h3><p>Remain Active &amp; Independent with our wide choice of walking aids from seat walkers, walking sticks &amp; crutches</p><div class="btn-green">READ MORE &nbsp;›</div></div>

<div class="abs product" style="left:262px;top:2880px"><h3>Everday Living Aids</h3><p>Maintain your freedom with our selection of shower chairs, commodes &amp; daily aids.</p><div class="btn-green">READ MORE &nbsp;›</div></div>
<div class="abs photo" style="left:645px;top:2800px;width:310px;height:380px" role="img" aria-label="Black commode chair with padded seat"></div>

<div class="abs photo" style="left:250px;top:3230px;width:300px;height:350px" role="img" aria-label="Consumer health products: insoles, blood pressure monitor, gel eye mask and knee brace"></div>
<div class="abs product" style="left:614px;top:3330px"><h3>Consumer Health</h3><p>Keep Healthy with our range of sports joint braces, gel insoles, relaxing eye masks &amp; heart BP monitors</p><div class="btn-green">READ MORE &nbsp;›</div></div>

<section class="abs testi">
  <h2 class="abs section-title">What the people say...</h2>
  <div class="abs arrow-c" style="left:455px;top:191px"><svg width="14" height="14" viewBox="0 0 14 14"><path d="M9 2 4 7l5 5" fill="none" stroke="#999" stroke-width="2"/></svg></div>
  <div class="abs avatar" role="img" aria-label="Portrait of a customer in a wheelchair"></div>
  <div class="abs arrow-c" style="left:697px;top:191px"><svg width="14" height="14" viewBox="0 0 14 14"><path d="m5 2 5 5-5 5" fill="none" stroke="#999" stroke-width="2"/></svg></div>
  <div class="abs qmark" style="left:295px;top:282px">“</div>
  <p class="abs quote">It is a long established fact that a reader will be distracted by the readable content of a page when looking at its layout. The point of using Lorem Ipsum is that it has a more-or-less normal distribution of letters, as opposed</p>
  <div class="abs qmark" style="left:755px;top:420px">”</div>
</section>

<section class="news">
  <h2 class="abs section-title" style="font-size:28px">Sign Up To Our Newsletter</h2>
  <div class="abs sub">Get more details to update</div>
  <div class="abs field" style="left:263px;width:238px">Name</div>
  <div class="abs field" style="left:517px;width:238px">E-mail id</div>
  <div class="abs btn-red">SIGNUP!</div>
</section>

<footer class="abs footer">
  <div class="abs brand"><span>TOLVENA CARE</span><i class="dot"></i></div>
  <div class="abs follow-row">FOLLOW US : <i></i><i style="background:#7cc6ee"></i><i style="background:#e88a7a"></i></div>
  <div class="abs fhead" style="left:597px;top:58px">CONTACT US</div>
  <div class="abs fline" style="left:600px;top:107px">⌖ <span>14 Wattle Street, Eastwood</span></div>
  <div class="abs fline" style="left:600px;top:143px">✆ <span>55014392</span></div>
  <div class="abs fline" style="left:600px;top:180px">✉ <span>info@tolvenacare.com</span></div>
  <div class="abs fhead" style="left:948px;top:58px">MENU</div>
  <ul class="abs fmenu" style="left:948px;top:92px"><li>Home</li><li>About us</li><li>Services</li><li>Rehabilitation aids</li><li>Mobility</li><li>Blog</li><li>Contact us</li></ul>
</footer>

<div class="abs copy">Copyright © 2017 All Rights Reserved</div>

</body>
</html>
```